Illustrationen für Versicherungsunternehmen
Zielgruppe
Versicherungsunternehmen. Zielgruppen sind sowohl Firmen als auch Privatpersonen in jeder Altersklasse.
Die hier adressierte Zielgruppe sind moderndenkende, kreative Mitarbeiter.
Aufgabenstellung
Es geht um die Visualisierung eines Team-Manifests bestehend aus 15 Prinzipien. Diese sollen möglichst ansprechend, kreativ, aber auch nicht zu verspielt dargestellt werden. Außerdem soll die Darstellung auch noch das bereits vorhandene Projektlogo (Anhang) enthalten, dieses soll auch nicht im Vordergrund/Fokus stehen.
Ein Beispiel für eine ähnliche Visualisierung ist im Anhang beigefügt, diese entspricht optisch sehr stark den Vorstellungen. Es soll am Ende eine Vorlage für ein Plakat entstehen, welches man in unterschiedlichen Formaten (DIN 4 bis DIN 0) erstellen kann. Bei der Farbgebung sollte die dominierende Farbe blau (Blautöne) sein, ergänzt durch orangefarbene Akzente. Die 15 Prinzipien sind der 2.Anlage zu entnehmen.

```html
<!DOCTYPE html>
<html lang="de">
<head>
<meta charset="utf-8">
<title>Team-Manifest – 15 Prinzipien</title>
<link rel="stylesheet" href="https://fonts.googleapis.com/css2?family=Russo+One&family=Quicksand:wght@500;600&family=Oswald:wght@500;600&family=Advent+Pro:wght@500;600&family=Saira+Condensed:wght@600;700&family=Courier+Prime:wght@700&family=Comfortaa:wght@500&family=Bungee&display=swap">
<style>
  :root {
    --blue: #1f5fe6;
    --orange: #ff7a1c;
    --paper: #ffffff;
  }
  html, body { margin: 0; padding: 0; overflow: hidden; background: var(--paper); }
  .manifest { display: block; width: 849px; height: 1200px; background: var(--paper); }
  .blue { fill: var(--blue); }
  .orange { fill: var(--orange); }
  .f-block { font-family: "Russo One", sans-serif; }
  .f-round { font-family: "Quicksand", sans-serif; font-weight: 600; }
  .f-tall { font-family: "Oswald", sans-serif; font-weight: 600; }
  .f-thin { font-family: "Advent Pro", sans-serif; font-weight: 600; }
  .f-cond { font-family: "Saira Condensed", sans-serif; font-weight: 700; }
  .f-mono { font-family: "Courier Prime", monospace; font-weight: 700; }
  .f-soft { font-family: "Comfortaa", sans-serif; font-weight: 500; }
  .f-stamp { font-family: "Bungee", sans-serif; }
  .light { font-weight: 500; }
</style>
</head>
<body>
<svg class="manifest" viewBox="0 0 849 1200" xmlns="http://www.w3.org/2000/svg" role="img" aria-label="Team-Manifest mit 15 Prinzipien">
  <!-- Kopfblock links -->
  <text class="f-block blue" x="29" y="93" font-size="62" textLength="364" lengthAdjust="spacingAndGlyphs">GEMEINSAM</text>
  <text class="f-round blue" x="29" y="154" font-size="58" textLength="364" lengthAdjust="spacingAndGlyphs">SIND WIR</text>
  <text class="f-block orange" x="29" y="264" font-size="128" textLength="385" lengthAdjust="spacingAndGlyphs">STÄRKER.</text>

  <!-- Kopfblock rechts -->
  <text class="f-round blue" x="428" y="75" font-size="52" textLength="399" lengthAdjust="spacingAndGlyphs">DENKBAR IST</text>
  <text class="f-round orange" x="428" y="122" font-size="52" textLength="399" lengthAdjust="spacingAndGlyphs">MACHBAR.</text>
  <text class="f-thin blue" x="421" y="207" font-size="66" textLength="404" lengthAdjust="spacingAndGlyphs">VERSPROCHEN IST</text>
  <text class="f-thin orange" x="421" y="271" font-size="86" textLength="404" lengthAdjust="spacingAndGlyphs">VERSPROCHEN</text>

  <text class="f-round blue" x="29" y="303" font-size="30" textLength="796" lengthAdjust="spacingAndGlyphs"><tspan font-weight="700">WIR</tspan> GESTALTEN <tspan font-weight="700">HEUTE</tspan> UND DENKEN AN MORGEN.</text>

  <rect class="blue" x="29" y="314" width="439" height="17" rx="3"/>
  <text class="f-round" x="478" y="334" font-size="26" textLength="347" lengthAdjust="spacingAndGlyphs"><tspan class="orange" font-weight="700">FAIR</tspan><tspan class="blue"> ODER GAR NICHT</tspan></text>

  <!-- Mittelteil links -->
  <text class="f-cond blue" x="36" y="382" font-size="38" textLength="193" lengthAdjust="spacingAndGlyphs">VERSPROCHEN</text>
  <text class="f-block blue" x="36" y="456" font-size="90" textLength="193" lengthAdjust="spacingAndGlyphs">IST</text>
  <text class="f-cond orange" x="36" y="493" font-size="38" textLength="193" lengthAdjust="spacingAndGlyphs">VERSPROCHEN.</text>

  <text class="f-block blue" x="29" y="560" font-size="42" textLength="212" lengthAdjust="spacingAndGlyphs">UNSERE</text>
  <text class="f-block orange" x="29" y="596" font-size="34" textLength="212" lengthAdjust="spacingAndGlyphs">VORSORGE</text>
  <text class="f-round blue" x="29" y="614" font-size="20" textLength="212" lengthAdjust="spacingAndGlyphs">braucht keinen Likör.</text>

  <!-- Mittelteil rechts -->
  <text class="f-block" x="250" y="383" font-size="36" textLength="575" lengthAdjust="spacingAndGlyphs"><tspan class="orange">GEMEINSAM</tspan><tspan class="blue"> SIND WIR </tspan><tspan class="orange">STÄRKER.</tspan></text>
  <text class="f-round light" x="250" y="432" font-size="44" textLength="575" lengthAdjust="spacingAndGlyphs"><tspan class="blue">FEHLER MACHEN IST </tspan><tspan class="orange">KEIN FEHLER.</tspan></text>
  <text class="f-block blue" x="254" y="517" font-size="76" textLength="571" lengthAdjust="spacingAndGlyphs">WIR SPRECHEN</text>
  <text class="f-tall orange" x="254" y="617" font-size="118" textLength="571" lengthAdjust="spacingAndGlyphs">KLARTEXT</text>

  <text class="f-round blue" x="29" y="656" font-size="30" textLength="796" lengthAdjust="spacingAndGlyphs">DIE PROBLEME UNSERER KUNDEN SIND UNSERE PROBLEME</text>

  <!-- Block drei Spalten -->
  <text class="f-tall orange" x="29" y="764" font-size="128" textLength="131" lengthAdjust="spacingAndGlyphs">FAIR</text>
  <text class="f-thin blue" x="29" y="811" font-size="54" textLength="131" lengthAdjust="spacingAndGlyphs">ODER</text>
  <text class="f-thin blue" x="29" y="854" font-size="46" textLength="131" lengthAdjust="spacingAndGlyphs">GAR NICHT</text>

  <text class="f-cond orange" x="183" y="721" font-size="68" textLength="300" lengthAdjust="spacingAndGlyphs">VERTRAUEN</text>
  <text class="f-mono blue" x="183" y="746" font-size="34" textLength="300" lengthAdjust="spacingAndGlyphs">um  zu</text>
  <text class="f-cond orange" x="183" y="806" font-size="66" textLength="300" lengthAdjust="spacingAndGlyphs">VERTRAUEN</text>
  <text class="f-cond blue" x="183" y="850" font-size="44" textLength="300" lengthAdjust="spacingAndGlyphs">DENKVERBOTE SIND TABU</text>

  <text class="f-block blue" x="499" y="695" font-size="30" textLength="326" lengthAdjust="spacingAndGlyphs">JEDES ARGUMENT ZÄHLT</text>
  <text class="f-block blue" x="499" y="763" font-size="66" textLength="326" lengthAdjust="spacingAndGlyphs">WIR HABEN</text>
  <text class="f-round light orange" x="499" y="799" font-size="34" textLength="326" lengthAdjust="spacingAndGlyphs">OFFENE OHREN FÜR</text>
  <text class="f-block orange" x="510" y="856" font-size="62" textLength="315" lengthAdjust="spacingAndGlyphs">NEUES</text>

  <!-- Trennband -->
  <rect class="blue" x="128" y="872" width="40" height="17" rx="3"/>
  <text class="f-block" x="178" y="895" font-size="34" textLength="496" lengthAdjust="spacingAndGlyphs"><tspan class="blue">GEMEINSAM</tspan><tspan class="blue" class="f-round"> sind wir </tspan><tspan class="orange">STÄRKER.</tspan></text>
  <rect class="blue" x="682" y="872" width="45" height="17" rx="3"/>

  <!-- Fußblock -->
  <text class="f-soft" x="29" y="953" font-size="42" textLength="571" lengthAdjust="spacingAndGlyphs"><tspan class="blue">Wir sprechen </tspan><tspan class="orange">Klartext</tspan></text>
  <text class="f-round" x="29" y="1013" font-size="52" textLength="571" lengthAdjust="spacingAndGlyphs"><tspan class="blue light">DENKBAR IST </tspan><tspan class="orange" font-weight="700">MACHBAR</tspan></text>

  <text class="f-stamp blue" x="625" y="966" font-size="46" textLength="200" lengthAdjust="spacingAndGlyphs">TRAU</text>
  <text class="f-stamp blue" x="638" y="1011" font-size="46" textLength="176" lengthAdjust="spacingAndGlyphs">DICH</text>

  <text class="f-block" x="29" y="1059" font-size="38" textLength="394" lengthAdjust="spacingAndGlyphs"><tspan class="blue">UNSERE </tspan><tspan class="orange">VORSORGE</tspan></text>
  <text class="f-round blue" x="29" y="1088" font-size="26" textLength="394" lengthAdjust="spacingAndGlyphs">braucht keinen Likör.</text>
  <text class="f-round" x="29" y="1126" font-size="32" textLength="394" lengthAdjust="spacingAndGlyphs"><tspan class="blue">VERSPROCHEN IST </tspan><tspan class="orange">VERSPROCHEN</tspan></text>

  <!-- Projektname -->
  <g class="project-mark">
    <rect class="blue" x="452" y="1070" width="40" height="40"/>
    <text class="f-round blue" x="452" y="1058" font-size="36" font-weight="700" textLength="290" lengthAdjust="spacingAndGlyphs">Wegweiser 2030</text>
  </g>

  <text class="f-block blue" x="29" y="1176" font-size="48" textLength="796" lengthAdjust="spacingAndGlyphs">WIR SIND ENTSCHEIDUNGSFREUDIG</text>
</svg>
</body>
</html>
```